Creative, fresh business card design for Brindlecrest Linings

We need a fresh, creative business card design for Brindlecrest Linings. We are the manufacturer of Brindlecrest Linings in Australia. Wall panels are 2400 x 1200mm panels made from MDF and feature 3D patterns on the face of the panel. The colours to be used are green, silver/grey and white RGB
Red 187
Green 207
Blue 65.

An idea is to possibly use a watermark of one of our designs as a background (like on the "Lattice" design on the left hand side of page 2 of our brochure).

Target Market(s)

Interior designers, architects, builders and home renovators

Industry/Entity Type

Business

Contact Information for Business Card

Details to go on the card are:
Our logo (attached),
Slogan: "Decorative panels for interiors and exteriors",
Contact name,
Position,
Mobile phone number,
Business address,
Business phone,
Business fax,
Website and
Email address.

I have attached a few images of our panels and our brochure for reference.

The colours of the business card should feature our logo colours which are: RGB
Red 187
Green 207
Blue 65

Requirements
Must have
• Very modern fonts and design. Some of the designs shown especially the "Weave" design which is a popular design.
Nice to have
• Creative but simple design. Very contemporary.
Should not have
• Anything ornate or old fashioned.

```html
<!DOCTYPE html>
<html lang="en">
<head>
<meta charset="utf-8">
<title>Brindlecrest Linings – Business Card</title>
<link rel="stylesheet" href="https://fonts.googleapis.com/css2?family=Open+Sans:wght@400;600;700&display=swap">
<style>
  :root {
    --page-bg: #e4e2df;
    --card-clear: #eef0ee;
    --card-frost: #dfe3e0;
    --brand-green: #bbcf41;
    --green-deep: #8fae22;
    --green-light: #c9dc5a;
    --swoosh-grey: #4d4f55;
    --ink-dark: #4a4c52;
    --ink-light: #ffffff;
    --ink-soft: #f4f7e6;
  }
  * { margin: 0; padding: 0; box-sizing: border-box; }
  html, body {
    width: 1200px; height: 969px; overflow: hidden;
    background: var(--page-bg);
    font-family: "Open Sans", Arial, sans-serif;
  }
  .canvas { position: relative; width: 1200px; height: 969px; }
  .business-card {
    position: absolute; left: 100px; top: 200px;
    width: 1000px; height: 568px;
    border-radius: 30px; overflow: hidden;
    background: linear-gradient(160deg, var(--card-clear), var(--card-frost));
    box-shadow: 0 18px 40px rgba(0,0,0,0.18);
  }
  .card-shapes { position: absolute; inset: 0; }
  .contact-name {
    position: absolute; left: 43px; top: 48px;
    font-size: 32px; font-weight: 700; letter-spacing: 0.5px;
    color: var(--ink-soft);
  }
  .contact-role {
    position: absolute; left: 43px; top: 92px;
    font-size: 25px; font-weight: 400; color: var(--ink-light);
  }
  .address {
    position: absolute; left: 43px; top: 298px;
    font-size: 24px; line-height: 36px; color: var(--ink-light);
  }
  .contact-list {
    position: absolute; left: 43px; top: 388px; list-style: none;
  }
  .contact-list li {
    display: flex; align-items: center; gap: 16px;
    height: 38px; font-size: 23px; color: var(--ink-soft);
  }
  .contact-list svg { width: 24px; height: 24px; fill: var(--ink-light); }
  .brand-block {
    position: absolute; left: 585px; top: 70px; width: 345px;
  }
  .brand-name {
    display: flex; align-items: center; gap: 16px;
    font-size: 33px; font-weight: 700; color: var(--ink-dark);
    line-height: 1.1;
  }
  .brand-square {
    flex: none; width: 70px; height: 70px; background: var(--brand-green);
  }
  .brand-bar {
    height: 10px; margin-top: 22px; background: var(--ink-dark);
  }
  .slogan {
    margin-top: 22px; text-align: center;
    font-size: 19px; line-height: 24px; letter-spacing: 2.4px;
    color: var(--ink-dark);
  }
</style>
</head>
<body>
<main class="canvas">
  <section class="business-card">
    <svg class="card-shapes" viewBox="0 0 1000 568" preserveAspectRatio="none" aria-hidden="true">
      <defs>
        <linearGradient id="greenPanel" x1="0" y1="0" x2="1" y2="1">
          <stop offset="0" stop-color="var(--green-light)"/>
          <stop offset="0.55" stop-color="var(--brand-green)"/>
          <stop offset="1" stop-color="var(--green-deep)"/>
        </linearGradient>
      </defs>
      <path class="swoosh-band" d="M400 0 H445 C 470 240, 640 440, 860 568 H 800 C 600 450, 430 260, 400 0 Z" fill="var(--swoosh-grey)"/>
      <path class="green-panel" d="M0 0 H410 C 440 250, 600 440, 815 568 H0 Z" fill="url(#greenPanel)"/>
    </svg>

    <h1 class="contact-name">OWEN CARRICK</h1>
    <p class="contact-role">CEO&amp;Founder</p>

    <p class="address">214 Harbour Row<br>Geelong, Victoria 3220</p>

    <ul class="contact-list">
      <li><svg viewBox="0 0 24 24"><path d="M6.6 10.8a15.1 15.1 0 0 0 6.6 6.6l2.2-2.2a1 1 0 0 1 1-.25 11.4 11.4 0 0 0 3.6.57 1 1 0 0 1 1 1V20a1 1 0 0 1-1 1A17 17 0 0 1 3 4a1 1 0 0 1 1-1h3.5a1 1 0 0 1 1 1c0 1.25.2 2.45.57 3.57a1 1 0 0 1-.25 1z"/></svg>(03) 5521 4807</li>
      <li><svg viewBox="0 0 24 24"><path d="M6 2h12v6H6zM4 9h16a2 2 0 0 1 2 2v6h-4v5H6v-5H2v-6a2 2 0 0 1 2-2zm4 7v4h8v-4z"/></svg>(03) 5521 4819</li>
      <li><svg viewBox="0 0 24 24"><path d="M2 5h20v14H2zm2 2v.5l8 5 8-5V7zm0 2.8V17h16V9.8l-8 5z"/></svg>ocarrick@brindlecrestlinings.com</li>
      <li><svg viewBox="0 0 24 24"><path d="M12 2a10 10 0 1 0 0 20 10 10 0 0 0 0-20zm6.9 6h-3a15 15 0 0 0-1.3-3.7A8 8 0 0 1 18.9 8zM12 4a13 13 0 0 1 1.9 4h-3.8A13 13 0 0 1 12 4zM4.3 14a8 8 0 0 1 0-4h3.4a16 16 0 0 0 0 4zm.8 2h3a15 15 0 0 0 1.3 3.7A8 8 0 0 1 5.1 16zm3-8h-3a8 8 0 0 1 4.3-3.7A15 15 0 0 0 8.1 8zM12 20a13 13 0 0 1-1.9-4h3.8A13 13 0 0 1 12 20zm2.3-6H9.7a14 14 0 0 1 0-4h4.6a14 14 0 0 1 0 4zm.3 5.7a15 15 0 0 0 1.3-3.7h3a8 8 0 0 1-4.3 3.7zm1.7-5.7a16 16 0 0 0 0-4h3.4a8 8 0 0 1 0 4z"/></svg>www.brindlecrestlinings.com</li>
    </ul>

    <div class="brand-block">
      <div class="brand-name"><span class="brand-square"></span>Brindlecrest Linings</div>
      <div class="brand-bar"></div>
      <p class="slogan">decorative panels for<br>interiors &amp; landscapes</p>
    </div>
  </section>
</main>
</body>
</html>
```